Rocket business card

Modern business card design, use of color is good with clean space too.

Things to include on card:

Quote: I add fuel to your optometry practice

- Eyewear Sales
- Admin Duties
- Revenue Collection
- Leadership
- Tech Adoption
- COGS Reduction
- Product Sourcing
-Medical Growth

Dalton Vessey, CEO
Glint Harbor
Text Me! 847-302-1964
dalton@glintharbor.example

```html
<!DOCTYPE html>
<html lang="en">
<head>
<meta charset="utf-8">
<title>Glint Harbor — Business Card</title>
<link rel="stylesheet" href="https://fonts.googleapis.com/css2?family=Raleway:wght@400;500&family=Source+Sans+3:wght@400;600&display=swap">
<style>
  :root {
    --backdrop: #22272a;
    --card-light: #ffffff;
    --card-mid: #eeeeee;
    --card-shade: #d6d6d6;
    --ink: #111111;
    --ink-soft: #555555;
    --flame-red: #c5401f;
    --flame-orange: #e07a1f;
    --flame-gold: #e89c18;
    --tagline-red: #d8382a;
  }
  * { box-sizing: border-box; margin: 0; padding: 0; }
  html, body {
    width: 1200px; height: 1176px; overflow: hidden;
    background: var(--backdrop);
    font-family: "Source Sans 3", Arial, sans-serif;
  }
  .card {
    position: absolute; left: 280px; width: 617px; height: 352px;
    border-radius: 22px; overflow: hidden;
    background: linear-gradient(200deg, var(--card-light) 0%, var(--card-mid) 55%, var(--card-shade) 100%);
  }
  .card--front { top: 190px; }
  .card--back { top: 591px; }

  .brand {
    position: absolute; left: 56px; top: 150px; width: 240px;
    display: flex; align-items: center; gap: 12px;
    font-family: "Raleway", Arial, sans-serif; font-weight: 500;
    font-size: 27px; letter-spacing: 1px; color: var(--ink);
    white-space: nowrap;
  }
  .brand__dot {
    width: 26px; height: 26px; border-radius: 50%;
    background: var(--flame-orange); flex: none;
  }

  .identity { position: absolute; left: 320px; top: 106px; }
  .identity__name {
    font-family: "Raleway", Arial, sans-serif; font-weight: 400;
    font-size: 25px; color: var(--ink-soft); line-height: 1;
  }
  .identity__role { font-size: 14px; vertical-align: 10px; margin-left: 2px; }
  .identity__tagline {
    margin-top: 6px; font-size: 15.5px;
    background: linear-gradient(90deg, var(--tagline-red), var(--flame-gold));
    -webkit-background-clip: text; background-clip: text; color: transparent;
  }
  .contact { list-style: none; margin-top: 16px; }
  .contact__item {
    display: flex; align-items: center; gap: 10px;
    font-size: 15px; color: var(--ink-soft); height: 26px;
  }
  .contact__icon { width: 14px; height: 14px; flex: none; }

  .back__art { position: absolute; left: 0; top: 0; }
  .services {
    list-style: none; position: absolute; left: 361px; top: 73px;
  }
  .services__item {
    display: flex; align-items: center; gap: 14px;
    height: 26.4px; font-size: 16px; color: var(--ink);
  }
  .services__mark {
    width: 14px; height: 14px; border-radius: 50%; flex: none;
    background: linear-gradient(135deg, var(--flame-red), var(--flame-gold));
    margin-left: 8px; margin-right: 8px;
  }
</style>
</head>
<body>
  <section class="card card--front">
    <div class="brand"><span class="brand__dot"></span>GLINT HARBOR</div>

    <div class="identity">
      <h1 class="identity__name">Dalton Vessey<span class="identity__role">CEO</span></h1>
      <p class="identity__tagline">I add fuel to your optometry practice</p>
      <ul class="contact">
        <li class="contact__item">
          <svg class="contact__icon" viewBox="0 0 16 16"><path fill="#d8502a" d="M2 6c0-2 3-3 6-3s6 1 6 3l-2 1-1-2H5L4 7 2 6zm2 2h8l1 5H3l1-5zm4 1.5a1.8 1.8 0 100 3.6 1.8 1.8 0 000-3.6z"/></svg>
          847-302-1964
        </li>
        <li class="contact__item">
          <svg class="contact__icon" viewBox="0 0 16 16"><rect x="2" y="4" width="12" height="8" fill="#e0662a"/><path d="M2 4l6 5 6-5" fill="none" stroke="#fff" stroke-width="1.2"/></svg>
          dalton@glintharbor.example
        </li>
        <li class="contact__item">
          <svg class="contact__icon" viewBox="0 0 16 16" fill="none" stroke="#e07a1f" stroke-width="1.2"><circle cx="8" cy="8" r="6"/><ellipse cx="8" cy="8" rx="2.6" ry="6"/><path d="M2 8h12M3 5h10M3 11h10"/></svg>
          glintharbor.example
        </li>
      </ul>
    </div>
  </section>

  <section class="card card--back">
    <svg class="back__art" width="617" height="352" viewBox="0 0 617 352" role="img" aria-label="Large rocket illustration on an orange flame-coloured disc">
      <defs>
        <linearGradient id="flame" x1="0" y1="0" x2="1" y2="0.3">
          <stop offset="0" stop-color="#c5401f"/>
          <stop offset="0.55" stop-color="#e07a1f"/>
          <stop offset="1" stop-color="#e89c18"/>
        </linearGradient>
      </defs>
      <circle cx="145" cy="172" r="176" fill="url(#flame)"/>
    </svg>

    <ul class="services">
      <li class="services__item"><span class="services__mark"></span>Eyewear Sales</li>
      <li class="services__item"><span class="services__mark"></span>Admin Duties</li>
      <li class="services__item"><span class="services__mark"></span>Revenue Collection</li>
      <li class="services__item"><span class="services__mark"></span>Leadership</li>
      <li class="services__item"><span class="services__mark"></span>Tech Adoption</li>
      <li class="services__item"><span class="services__mark"></span>COGS Reduction</li>
      <li class="services__item"><span class="services__mark"></span>Product Sourcing</li>
      <li class="services__item"><span class="services__mark"></span>Medical Growth</li>
    </ul>
  </section>
</body>
</html>
```